Mox Dune Reel Business cards

Logo, tag line and photo on card
Agent Name
Title
Address
Phone number
Email
Website
Make logo on one side large by rotating  to portrait format.  Keep the background of the logo white.

Contact Information for Business Card
Slogan; Shaping Every Mox Ahead

```html
<!DOCTYPE html>
<html lang="en">
<head>
<meta charset="utf-8">
<title>Mox Dune Reel – Business Cards</title>
<link href="https://fonts.googleapis.com/css2?family=Montserrat:wght@400;500;700;800&display=swap" rel="stylesheet">
<style>
  :root {
    --backdrop: #232323;
    --card: #ffffff;
    --navy: #1f2a63;
    --red: #c8202a;
    --ink: #1c1c1c;
    --photo-a: #8a847c;
    --photo-b: #3a3632;
  }
  * { box-sizing: border-box; margin: 0; padding: 0; }
  html, body { width: 1200px; height: 711px; overflow: hidden; }
  body {
    background: var(--backdrop);
    font-family: "Montserrat", sans-serif;
    display: flex;
    justify-content: center;
    align-items: center;
    gap: 70px;
  }
  .card {
    width: 320px;
    height: 540px;
    background: var(--card);
    border-radius: 26px;
    box-shadow: 0 14px 30px rgba(0,0,0,.55);
    display: flex;
    flex-direction: column;
    align-items: center;
  }
  .wordmark {
    color: var(--navy);
    font-weight: 800;
    text-align: center;
    letter-spacing: -0.02em;
  }
  .tagline {
    color: var(--ink);
    font-weight: 500;
    text-align: center;
  }

  /* Front */
  .card--front { justify-content: center; gap: 26px; }
  .card--front .wordmark { font-size: 66px; line-height: 0.98; }
  .card--front .tagline { font-size: 16px; }

  /* Back */
  .card--back { padding-top: 40px; }
  .card--back .wordmark { font-size: 30px; line-height: 1; }
  .card--back .tagline { font-size: 12.5px; margin-top: 12px; }
  .portrait {
    width: 118px; height: 118px;
    border-radius: 50%;
    margin-top: 22px;
    background: radial-gradient(circle at 50% 38%, var(--photo-a), var(--photo-b));
  }
  .agent-name {
    margin-top: 18px;
    color: var(--navy);
    font-weight: 800;
    font-size: 19px;
    letter-spacing: 0.02em;
  }
  .agent-title { font-size: 13px; color: var(--ink); margin-top: 2px; }
  .icon-rule {
    display: flex; align-items: center; gap: 6px;
    width: 250px; margin-top: 16px;
  }
  .icon-rule .rule { flex: 1; height: 1.5px; background: var(--navy); }
  .icon {
    width: 26px; height: 24px; border-radius: 6px;
    background: var(--navy);
    display: flex; align-items: center; justify-content: center;
  }
  .contacts {
    margin-top: 12px; text-align: center;
    font-size: 13px; line-height: 1.45; color: var(--ink);
  }
  .divider { width: 250px; height: 1.5px; background: var(--navy); margin-top: 14px; }
  .address {
    margin-top: 10px; text-align: center;
    font-size: 13px; line-height: 1.4; color: var(--ink);
  }
</style>
</head>
<body>
  <section class="card card--front">
    <div class="wordmark">Mox<br>Dune<br>Reel</div>
    <p class="tagline">Shaping Every Mox Ahead</p>
  </section>

  <section class="card card--back">
    <div class="wordmark">Mox<br>Dune<br>Reel</div>
    <p class="tagline">Shaping Every Mox Ahead</p>
    <div class="portrait" role="img" aria-label="Portrait photo of the agent"></div>
    <h1 class="agent-name">ELIAS VARNER</h1>
    <p class="agent-title">Managing Director</p>
    <div class="icon-rule">
      <span class="rule"></span>
      <span class="icon"><svg width="14" height="14" viewBox="0 0 24 24" fill="#fff"><path d="M6.6 10.8a15 15 0 0 0 6.6 6.6l2.2-2.2a1 1 0 0 1 1-.25 11.4 11.4 0 0 0 3.6.57 1 1 0 0 1 1 1V20a1 1 0 0 1-1 1A17 17 0 0 1 3 4a1 1 0 0 1 1-1h3.5a1 1 0 0 1 1 1c0 1.25.2 2.45.57 3.57a1 1 0 0 1-.25 1z"/></svg></span>
      <span class="icon"><svg width="14" height="12" viewBox="0 0 24 18" fill="none" stroke="#fff" stroke-width="2.4"><rect x="1.5" y="1.5" width="21" height="15" rx="1.5"/><path d="M2 2l10 8 10-8"/></svg></span>
      <span class="icon"><svg width="14" height="14" viewBox="0 0 24 24" fill="none" stroke="#fff" stroke-width="2"><circle cx="12" cy="12" r="9.5"/><path d="M2.5 12h19M12 2.5c3 3 3 16 0 19M12 2.5c-3 3-3 16 0 19"/></svg></span>
      <span class="rule"></span>
    </div>
    <div class="contacts">
      <p>123 456 789</p>
      <p>info@moxdunereel.com</p>
      <p>www.moxdunereel.com</p>
    </div>
    <div class="divider"></div>
    <div class="address">
      <p>Your address,</p>
      <p>City State, Zip 1234</p>
    </div>
  </section>
</body>
</html>
```